Custom Manufacturing Job Shop

We are looking for a business card design for Tall Oak Fabricators Inc. Tall Oak is a family owned business that manufactures any custom product to fit a customers needs, whether it is custom 1 piece or production parts, we truly take on projects that others just cant do. to help in your design go to www.talloakfab.example for a more in depth idea. we have the following capabilities that we would like to see on the card somewhere...maybe on the back of a 2 sided card? we are fully open to ideas.
Machining
• Fabrication
• Millwork
• Maintenance
• Laser Cutting
• Precision Forming
Engineering
Blasting/Painting

No matter how big or small, We literally do it all

preferably black or darker cards but we don't mind to see some color if you see a better fit. we are interested in looking at anything that catches attention.
I have attached our logo, if it is needed in a different file type please let me know and I will send it to you if I can. maybe adding some type of drawing or dimensional lines would be something to add?? just throwing ideas out there....
Updates

Reason: I added one of our shredder designs and would like to see a few more cards if possible using this. any questions please don't hesitate to ask!!

Target Market(s)

anyone looking for design/manufacturing/machining whether it is custom 1 off parts or production.

Industry/Entity Type

Business

Contact Information for Business Card

preferably darker shades, but also not opposed to some color in the same sense....not too bright

Font styles to use
Serif
Sans Serif

Requirements
Must have
• Gus Marrow
• Direct:555-312-7781
• Cell:555-298-4410
• Fax: 555-367-1925
• 42 Quarry Lane
• Dunmoreville, PA 17000
• I also would request having it in a format I can give to the company making the business cards to edit names/numbers etc. for the entire staff.
Nice to have
• drafting lines? we are open to almost anything....
Should not have
• exotic colors

```html
<!DOCTYPE html>
<html lang="en">
<head>
<meta charset="utf-8">
<title>Tall Oak Fabricators Inc. – Business Card</title>
<link rel="stylesheet" href="https://fonts.googleapis.com/css2?family=Michroma&display=swap">
<style>
  :root {
    --backdrop: #e4e4e4;
    --card: #fbfbfb;
    --ink: #3a3a3a;
    --ink-soft: #555555;
    --rule: #8a8a8a;
    --wave-dark: #b9b9b9;
    --wave-light: #dcdcdc;
  }
  * { margin: 0; padding: 0; box-sizing: border-box; }
  html, body {
    width: 1200px; height: 900px; overflow: hidden;
    background: var(--backdrop);
    font-family: "Michroma", sans-serif;
    color: var(--ink);
  }
  .card {
    position: absolute; left: 100px; top: 164px;
    width: 1000px; height: 572px;
    background: var(--card);
    border-radius: 44px;
    overflow: hidden;
    box-shadow: 0 10px 30px rgba(0,0,0,0.18);
  }
  .card__waves { position: absolute; left: 0; bottom: 0; width: 1000px; height: 572px; }
  .brand {
    position: absolute; left: 400px; top: 96px;
    display: flex; flex-direction: column; align-items: flex-start;
  }
  .brand__row { display: flex; align-items: center; gap: 16px; }
  .brand__mark {
    width: 34px; height: 34px; border-radius: 50%;
    background: var(--ink-soft);
  }
  .brand__name { font-size: 40px; letter-spacing: 2px; color: var(--ink); }
  .brand__url { margin-top: 8px; margin-left: 50px; font-size: 11px; letter-spacing: 3px; color: var(--rule); }
  .person {
    position: absolute; right: 560px; top: 248px;
    text-align: right;
  }
  .person__name { font-size: 22px; letter-spacing: 2px; }
  .person__title { margin-top: 10px; font-size: 14px; letter-spacing: 2px; color: var(--ink-soft); }
  .person__address { margin-top: 34px; font-size: 14px; line-height: 1.8; letter-spacing: 1.5px; color: var(--ink-soft); }
  .divider {
    position: absolute; left: 466px; top: 244px;
    width: 1px; height: 170px; background: var(--rule);
  }
  .contact { position: absolute; left: 490px; top: 248px; list-style: none; }
  .contact__item {
    display: flex; align-items: center; gap: 10px;
    font-size: 15px; letter-spacing: 1.5px; line-height: 32px;
    color: var(--ink);
  }
  .contact__icon { width: 16px; height: 16px; flex: none; }
</style>
</head>
<body>
  <main class="card">
    <svg class="card__waves" viewBox="0 0 1000 572" aria-hidden="true">
      <path d="M0 330 C 180 420, 420 500, 1000 500 L1000 572 L0 572 Z" fill="var(--wave-light)"/>
      <path d="M0 372 C 200 470, 460 535, 1000 530 L1000 572 L0 572 Z" fill="var(--wave-dark)"/>
      <path d="M0 420 C 220 510, 480 560, 1000 558 L1000 572 L0 572 Z" fill="var(--card)"/>
    </svg>

    <header class="brand">
      <div class="brand__row">
        <span class="brand__mark"></span>
        <span class="brand__name">TALL OAK FAB</span>
      </div>
      <span class="brand__url">talloakfab.example</span>
    </header>

    <section class="person">
      <p class="person__name">Gus Marrow</p>
      <p class="person__title">Owner - C.E.O</p>
      <p class="person__address">42 Quarry Lane<br>Dunmoreville, PA 17000</p>
    </section>

    <div class="divider"></div>

    <ul class="contact">
      <li class="contact__item">
        <svg class="contact__icon" viewBox="0 0 16 16"><circle cx="8" cy="8" r="8" fill="var(--ink)"/><path d="M5 4h2l1 2-1 1c.5 1 1.5 2 2.5 2.5l1-1 2 1v2c-4 0-7.5-3.5-7.5-7.5z" fill="var(--card)"/></svg>
        555-312-7781
      </li>
      <li class="contact__item">
        <svg class="contact__icon" viewBox="0 0 16 16"><circle cx="8" cy="8" r="8" fill="var(--ink)"/><rect x="5.5" y="3.5" width="5" height="9" rx="1" fill="var(--card)"/></svg>
        555-298-4410
      </li>
      <li class="contact__item">
        <svg class="contact__icon" viewBox="0 0 16 16"><circle cx="8" cy="8" r="8" fill="var(--ink)"/><rect x="4" y="6" width="8" height="5" fill="var(--card)"/><rect x="5.5" y="3.5" width="5" height="2.5" fill="var(--card)"/></svg>
        555-367-1925
      </li>
      <li class="contact__item">
        <svg class="contact__icon" viewBox="0 0 16 16"><circle cx="8" cy="8" r="8" fill="var(--ink)"/><rect x="4" y="5" width="8" height="6" fill="var(--card)"/><path d="M4 5l4 3.5 4-3.5" fill="none" stroke="var(--ink)" stroke-width="1"/></svg>
        gus@talloakfab.example
      </li>
      <li class="contact__item">
        <svg class="contact__icon" viewBox="0 0 16 16"><circle cx="8" cy="8" r="8" fill="var(--ink)"/><circle cx="8" cy="8" r="4.5" fill="none" stroke="var(--card)" stroke-width="1.2"/><path d="M3.5 8h9M8 3.5v9" stroke="var(--card)" stroke-width="1"/></svg>
        www.talloakfab.example
      </li>
    </ul>
  </main>
</body>
</html>
```